QR TILL WORKS , CREDIT CARD PROCESSING EQUIPMENT

qrtillworks is a sub division of Tallow a credit car processing co.
owen tasker
14 cedar hollow ln
alder falls 07312
suite 412

qrtillworks.example
cell 555-214-7730
office 555-861-2093
we sell pos systems to merchant who want to accept credit cards at there retail location.
black card would be nice buit open to different ideas

Target Market(s)

retail merchants

Industry/Entity Type

credit card processing

Contact Information for Business Card

card should include web site phone address

Colors

Designer to choose colors to be used in the design.

Requirements
Should not have
• red

```html
<!DOCTYPE html>
<html lang="en">
<head>
<meta charset="utf-8">
<title>QR Till Works — Business Card</title>
<link rel="stylesheet" href="https://fonts.googleapis.com/css2?family=Poppins:wght@400;500;600;700&display=swap">
<style>
  :root {
    --stage: #26262b;
    --card: #202326;
    --card-edge: #2a2d31;
    --white: #f4f4f2;
    --gold: #f0c021;
    --emboss: #34373b;
    --rule: #9a9ca0;
  }
  * { box-sizing: border-box; margin: 0; padding: 0; }
  html, body { width: 1200px; height: 800px; overflow: hidden; }
  body {
    background: var(--stage);
    font-family: "Poppins", sans-serif;
    display: flex;
    align-items: center;
    justify-content: center;
    gap: 40px;
  }
  .card {
    position: relative;
    width: 520px;
    height: 298px;
    background: var(--card);
    border: 1px solid var(--card-edge);
    border-radius: 22px;
  }
  .card--front {
    display: flex;
    align-items: center;
    justify-content: center;
  }
  .brand-name {
    font-weight: 600;
    letter-spacing: 0.5px;
    line-height: 1;
    text-transform: uppercase;
  }
  .card--front .brand-name {
    font-size: 38px;
    color: var(--emboss);
  }
  .card--back .brand-name {
    position: absolute;
    left: 40px;
    top: 112px;
    width: 190px;
    font-size: 30px;
    color: var(--white);
  }
  .divider {
    position: absolute;
    left: 252px;
    top: 72px;
    width: 1px;
    height: 120px;
    background: var(--rule);
  }
  .contact {
    position: absolute;
    left: 274px;
    top: 70px;
    color: var(--white);
  }
  .contact__name {
    font-size: 19px;
    font-weight: 700;
    color: var(--gold);
    letter-spacing: 0.3px;
    line-height: 1.1;
  }
  .contact__role {
    font-size: 12px;
    font-weight: 400;
    margin-bottom: 12px;
  }
  .contact__line {
    font-size: 12px;
    line-height: 1.5;
  }
  .contact__label {
    color: var(--gold);
    font-weight: 600;
  }
  .contact__web {
    margin-top: 12px;
    font-size: 12px;
    color: var(--gold);
  }
  .address {
    position: absolute;
    left: 30px;
    right: 30px;
    bottom: 30px;
    font-size: 13px;
    letter-spacing: 1.6px;
    color: var(--white);
    text-align: center;
    white-space: nowrap;
  }
</style>
</head>
<body>
  <section class="card card--front" aria-label="Card front">
    <p class="brand-name">QR Till Works</p>
  </section>

  <section class="card card--back" aria-label="Card back">
    <p class="brand-name">QR Till Works</p>
    <span class="divider"></span>
    <div class="contact">
      <p class="contact__name">OWEN TASKER</p>
      <p class="contact__role">Manager</p>
      <p class="contact__line"><span class="contact__label">CELL:</span> 555-214-7730</p>
      <p class="contact__line"><span class="contact__label">OFFICE:</span> 555-861-2093</p>
      <p class="contact__web">qrtillworks.example</p>
    </div>
    <p class="address">14 cedar hollow ln, alder falls 07312, suite 412</p>
  </section>
</body>
</html>
```